Sunvale Ride Co Splashpage

This webpage will be a holding page until our website is complete. This page needs to be designed to advertise our tours in Honolulu, Hawaii. So it is important to have prices displayed and have a Hawaiian theme.

1. Warm colors - suggest reds?
2. Hawaiian flower incorporated in design

3. Display prices
Adult - single Journey - $20
Adult - 1 Day - $20 (this needs to be displayed as a special deal/price because full price is $25)
Adult - 2 days - $30

Seniors - (62+) 1 Day + 1 Day Free - $20

Children 5 - 17 yrs - 1 Day - $13
Children 5 - 17 yrs - 2 Days - $15
Under 5 Yrs - Free

There will be an online booking button (text on button should say "Book Online", so please make sure it is clear where they can purchase the tickets.

3. A photo of our branded double decker bus should be incorporate on the page.

4. Our Message "Welcome to Sunvale Ride Co. Our Open Top Bus ensures you have an unrivalled view of Honolulu and all that this great city has to offer. We pass all of the city’s main sites, offering fantastic photo opportunities along the way. Our tour takes around 90 minutes. You can get on and off the bus as often as you want. Your ticket is valid for one or two days. All departures have commentary in English. If it’s raining, we have a sliding roof to keep you dry. Step on-board and let us show you the best of Honolulu."

5. Some tour sites our tour visits are: Marlow's Arcade, Waikiki beach, Umerik Palace, Bretoma Palace/King statue, Darvin's statue

We are catering to an international adult audience (ranging from 25 - 60 yrs of age) that handles vacation planning.

Please visit www.ridebyloop.ee to get an idea of our style.

• 1. prices displayed where they be viewed easily - There will be an online booking button so please make sure it is clear where they can purchase the tickets.

2. Adult - 1 Day - $20 (this needs to be displayed as a special deal/price because full price is $25)

3. Photo of our double decker bus

4. Hawaiian flower incorporated in design

5. Bright colors (make sure orange isn't the main background color) but not overwhelming

6. Logo on webpage
• 1. Images of our tour sites
2. Other Hawaiian images such as palm trees, Maile Lei, Sun with sunglasses, flower lei, parrot, Hawaiian sunsets
• -Do not want any shade of orange as the main background color

```html
<!DOCTYPE html>
<html lang="en">
<head>
<meta charset="utf-8">
<title>Sunvale Ride Co – Honolulu Open Top Tours</title>
<link href="https://fonts.googleapis.com/css2?family=Luckiest+Guy&family=Noto+Sans:wght@400;700&family=Titillium+Web:wght@400;600;700&display=swap" rel="stylesheet">
<style>
:root{
  --red:#b30f0c;
  --red-dark:#8c0a08;
  --maroon:#8e0a24;
  --maroon-dark:#5e0414;
  --orange:#e9760f;
  --orange-dark:#c65200;
  --yellow:#ffd233;
  --yellow-text:#f4d52b;
  --sky:#dfe9f1;
  --panel:#f4f5f7;
  --table-bg:#e2ddd8;
  --form-bg:#e8e4df;
  --border:#b1454a;
  --ink:#2a2a2a;
  --muted:#555;
  --road:#7a7a7a;
  --link:#3d6cc0;
}
*{box-sizing:border-box;margin:0;padding:0}
html,body{width:1198px;height:1200px;overflow:hidden;background:#fff}
body{position:relative;font-family:"Noto Sans",sans-serif;color:var(--ink)}
.abs{position:absolute}

/* header */
.site-header{left:0;top:0;width:1198px;height:108px;background:linear-gradient(#c0110e,#a50c0a 88%,#7e0806)}
.brand{left:72px;top:14px;display:flex;align-items:center;gap:14px}
.brand-dot{width:62px;height:62px;border-radius:50%;background:#f7c46a}
.brand-name{font-family:"Titillium Web",sans-serif;font-weight:700;font-size:44px;color:#fff;letter-spacing:.5px}
.language{left:782px;top:12px;width:312px;height:32px;border:2px solid #7b0705;border-radius:4px;background:#a00c0a;display:flex;align-items:center;padding-left:14px;gap:8px}
.language-label{font-family:"Noto Sans",sans-serif;font-weight:700;font-size:12px;color:#fff;margin-right:6px;letter-spacing:.4px}
.flag{width:18px;height:12px;display:block;border:1px solid #fff}
.flag.en{background:linear-gradient(90deg,#1a3a8a 40%,#fff 40% 60%,#1a3a8a 60%)}
.flag.fr{background:linear-gradient(90deg,#1f3c9c 33%,#fff 33% 66%,#d3202a 66%)}
.flag.it{background:linear-gradient(90deg,#1a8c3a 33%,#fff 33% 66%,#d3202a 66%)}
.flag.es{background:linear-gradient(#c8171e 25%,#f6c21a 25% 75%,#c8171e 75%)}
.flag.de{background:linear-gradient(#111 33%,#d3202a 33% 66%,#f2c21a 66%)}
.flag.se{background:linear-gradient(90deg,#1f5fb0 30%,#f6cc1a 30% 45%,#1f5fb0 45%)}
.flag.ru{background:linear-gradient(#fff 33%,#2a45b0 33% 66%,#d3202a 66%)}

/* hero */
.hero-sky{left:0;top:108px;width:1198px;height:540px;background:linear-gradient(#cfdde9,#e8eef3 60%,#eef0f2)}
.hero-panel{left:95px;top:108px;width:1008px;height:520px;background:linear-gradient(rgba(255,255,255,.85),rgba(255,255,255,.55))}
.intro{left:108px;top:150px;width:450px;font-size:14px;line-height:18.5px;color:#333}
.features{left:116px;top:224px;width:440px;list-style:none}
.features li{position:relative;padding-left:33px;font-size:14px;line-height:18.5px;color:#222;margin-bottom:17.5px}
.features li::before{content:"";position:absolute;left:0;top:2px;width:14px;height:14px;border-radius:50%;border:2px solid #b5465a;background:#f4e3e6}
.tagline{left:118px;top:494px;font-family:"Luckiest Guy",sans-serif;font-size:26px;line-height:37px;color:var(--yellow-text);text-shadow:2px 2px 0 #5b3b0b,-1px -1px 0 #5b3b0b,1px -1px 0 #5b3b0b,-1px 1px 0 #5b3b0b}
.polaroid{background:#fff;padding:7px 7px 22px;box-shadow:2px 3px 8px rgba(0,0,0,.35)}
.polaroid span{display:block;width:100%;height:100%}
.road{left:0;top:600px;width:1198px;height:120px}
.bus-photo{left:598px;top:338px;width:580px;height:372px;border-radius:30px 60px 20px 20px;background:linear-gradient(100deg,#b8170f,#d92a1c 45%,#9e0f0b 80%,#5a0a08)}

/* packages */
.packages{left:107px;top:630px;width:488px;height:382px;border:1px solid var(--border);border-radius:6px;background:var(--table-bg);box-shadow:0 4px 12px rgba(0,0,0,.15);overflow:hidden}
.packages-title{height:64px;background:linear-gradient(#f08a1c,var(--orange) 55%,var(--orange-dark));text-align:center;font-family:"Luckiest Guy",sans-serif;font-size:36px;line-height:70px;color:#fff;letter-spacing:.5px}
.price-table{border-collapse:collapse;width:100%;font-family:"Titillium Web",sans-serif}
.price-table thead th{height:42px;background:linear-gradient(var(--maroon),var(--maroon-dark));color:#fff;font-weight:400;font-size:19px}
.price-table td{height:65px;text-align:center;font-family:"Noto Sans",sans-serif;font-size:12.5px;color:#222;border-left:1px dashed #9a8c86;vertical-align:middle}
.price-table td:first-child{border-left:none;text-align:left;padding-left:35px}
.group{font-family:"Titillium Web",sans-serif;font-size:19px;color:#222;line-height:20px;display:block}
.age{font-size:11px;color:#333}
.deal{position:absolute;left:248px;top:121px;width:103px;height:46px;border:1px solid #b58a1a;border-radius:4px;background:linear-gradient(#ffe05a,#ffc21a);text-align:center}
.deal-old{font-size:12px;color:#c21b1b;text-decoration:line-through;margin-right:5px;vertical-align:3px}
.deal-new{font-family:"Titillium Web",sans-serif;font-weight:700;font-size:20px;color:#fff;text-shadow:1px 1px 0 #6b4a07}
.deal-badge{display:block;margin:0 auto;width:90px;font-size:7px;letter-spacing:1.5px;background:#fff;border:1px solid #555;border-radius:7px;line-height:10px;color:#333}
.senior-offer{position:absolute;left:248px;top:194px;width:230px;height:39px;border:1px solid #b58a1a;border-radius:3px;background:linear-gradient(#ffe05a,#ffc21a);text-align:center;line-height:39px;font-size:13px;color:#3a2a00}

/* reservation */
.reservation{left:595px;top:714px;width:499px;height:279px;border:1px solid var(--border);border-left:none;border-radius:0 6px 6px 0;background:var(--form-bg)}
.reservation h2{position:absolute;left:22px;top:14px;font-family:"Titillium Web",sans-serif;font-weight:400;font-size:19px;color:#333}
.field-head{position:absolute;top:55px;font-size:12.5px;font-weight:700;color:#333}
.field-label{position:absolute;width:60px;text-align:right;font-size:12.5px;color:#333}
.field-box{position:absolute;width:42px;height:25px;border:1px solid #999;border-radius:3px;background:linear-gradient(#e8e8e8,#fafafa)}
.field-arrow{position:absolute;width:20px;height:20px;border-radius:50%;border:1px solid #aaa;background:#f4f4f4}
.field-arrow::after{content:"";position:absolute;left:5px;top:7px;border-left:4.5px solid transparent;border-right:4.5px solid transparent;border-top:6px solid #333}
.date-box{position:absolute;left:210px;top:84px;width:183px;height:25px;border:1px solid #999;border-radius:3px;background:linear-gradient(#e8e8e8,#fafafa)}
.calendar{position:absolute;left:398px;top:81px;width:28px;height:28px;border:1px solid #bbb;border-radius:3px;background:#fff}
.book-btn{left:806px;top:844px;width:293px;height:106px;border-radius:4px;background:linear-gradient(#a80d25,var(--maroon) 60%,#76061a);box-shadow:0 2px 4px rgba(0,0,0,.3);display:flex;align-items:center;justify-content:center;gap:12px;color:#fff;font-family:"Titillium Web",sans-serif;font-size:26px;text-decoration:none}
.book-arrow{width:34px;height:34px;border-radius:50%;background:#f2f2f2;position:relative}
.terms{position:absolute;left:212px;top:244px;width:280px;font-size:10px;line-height:12.5px;color:#333}
.terms a{color:var(--link);text-decoration:none}

/* footer */
.footer-rule{left:94px;top:1075px;width:1011px;height:1px;background:#9a9a9a}
.footer-info{left:105px;top:1092px;font-size:11.5px;font-weight:700;color:#555}
.footer-links{right:102px;top:1092px;font-size:11.5px;font-weight:700;color:#555}
.footer-links a{color:#555;text-decoration:none}
</style>
</head>
<body>

<header class="site-header abs">
  <div class="brand abs"><span class="brand-dot"></span><span class="brand-name">Sunvale Ride Co</span></div>
  <nav class="language abs" aria-label="Language">
    <span class="language-label">LANGUAGE</span>
    <span class="flag en"></span><span class="flag fr"></span><span class="flag it"></span><span class="flag es"></span><span class="flag de"></span><span class="flag se"></span><span class="flag ru"></span>
  </nav>
</header>

<div class="hero-sky abs"></div>
<div class="hero-panel abs"></div>

<p class="intro abs">Welcome to Sunvale Ride Co. Our Open Top Bus ensures you have an unrivalled view of Honolulu and all that this great city has to offer.</p>

<ul class="features abs">
  <li>We pass all of the city’s main sites, offering fantastic photo opportunities along the way.</li>
  <li>Our tour takes around 90 minutes.</li>
  <li>You can get on and off the bus as often as you want.</li>
  <li>Your ticket is valid for one or two days.</li>
  <li>All departures have commentary in English.</li>
  <li>If it’s raining, we have a sliding roof to keep you dry.</li>
</ul>

<p class="tagline abs">Step on-board and let us show you<br>the best of Honolulu</p>

<div class="polaroid abs" style="left:538px;top:168px;width:112px;height:170px;transform:rotate(-8deg)"><span role="img" aria-label="Clock tower at the harbour" style="background:linear-gradient(#cfe0ef,#e9eef2)"></span></div>
<div class="polaroid abs" style="left:642px;top:195px;width:106px;height:124px"><span role="img" aria-label="Palm trees at a Hawaiian sunset" style="background:linear-gradient(#e7a46c,#b24a3a 60%,#3b1a16)"></span></div>
<div class="polaroid abs" style="left:826px;top:96px;width:128px;height:152px;transform:rotate(3deg)"><span role="img" aria-label="Marlow's Arcade with palm trees" style="background:linear-gradient(#9cc0d8,#d7a5a5 55%,#6b7d4f)"></span></div>
<div class="polaroid abs" style="left:950px;top:66px;width:132px;height:164px;transform:rotate(10deg)"><span role="img" aria-label="Waikiki beach and Diamond Head" style="background:linear-gradient(#5fa0d8,#2a7fb7 50%,#d8c9a4)"></span></div>
<div class="polaroid abs" style="left:785px;top:200px;width:114px;height:116px;transform:rotate(-12deg)"><span role="img" aria-label="Palms at dusk on the coast" style="background:linear-gradient(#566070,#b89a6c 70%,#3b3528)"></span></div>
<div class="polaroid abs" style="left:868px;top:228px;width:70px;height:80px;transform:rotate(-14deg)"><span role="img" aria-label="Bretoma Palace" style="background:linear-gradient(#a6c2da,#d0cbbd)"></span></div>
<div class="polaroid abs" style="left:718px;top:252px;width:92px;height:110px;transform:rotate(12deg)"><span role="img" aria-label="Umerik Palace" style="background:linear-gradient(#7fa6cf,#c7c3b6 60%,#6a6f52)"></span></div>
<div class="polaroid abs" style="left:792px;top:305px;width:66px;height:62px;transform:rotate(22deg)"><span role="img" aria-label="Darvin's statue" style="background:linear-gradient(#98b4cc,#8a7a6a)"></span></div>

<svg class="road abs" viewBox="0 0 1198 120" aria-hidden="true">
  <path d="M0 26 C300 -4 600 0 900 44 C1020 62 1120 60 1198 46 L1198 120 L0 120 Z" fill="var(--road)"/>
  <path d="M0 60 C300 36 600 40 900 80 C1020 96 1120 96 1198 88 L1198 120 L0 120 Z" fill="#fff"/>
</svg>

<div class="bus-photo abs" role="img" aria-label="Red branded open-top double decker tour bus with tropical flower livery"></div>

<section class="packages abs">
  <div class="packages-title">Tour Packages</div>
  <table class="price-table">
    <thead><tr><th style="width:124px"></th><th style="width:118px">1 Journey</th><th style="width:120px">1 Day</th><th>2 Days</th></tr></thead>
    <tbody>
      <tr><td><span class="group">Adult</span><span class="age">Age 17 - 62</span></td><td>$ 20</td><td></td><td>$ 30</td></tr>
      <tr><td><span class="group">Seniors</span><span class="age">Age 62+</span></td><td></td><td></td><td></td></tr>
      <tr><td><span class="group">Children</span><span class="age">Age 5 - 17</span></td><td></td><td>$ 13</td><td>$ 15</td></tr>
      <tr><td><span class="group">Kids</span><span class="age">Age &lt; 5</span></td><td>free</td><td>free</td><td>free</td></tr>
    </tbody>
  </table>
  <div class="deal"><span class="deal-old">$ 25</span><span class="deal-new">$ 20</span><span class="deal-badge">SPECIAL PRICE</span></div>
  <div class="senior-offer"><b>$ 20</b> &nbsp;( 2nd day <b>free !</b> )</div>
</section>

<section class="reservation abs">
  <h2>Online Reservation</h2>
  <span class="field-head" style="left:22px">Tour Participant</span>
  <span class="field-head" style="left:210px">Date</span>
  <span class="field-label" style="left:22px;top:58px;margin-top:28px">Adult</span>
  <span class="field-box" style="left:97px;top:84px"></span><span class="field-arrow" style="left:143px;top:86px"></span>
  <span class="field-label" style="left:22px;top:132px">Senior</span>
  <span class="field-box" style="left:97px;top:129px"></span><span class="field-arrow" style="left:143px;top:131px"></span>
  <span class="field-label" style="left:22px;top:180px">Children</span>
  <span class="field-box" style="left:97px;top:177px"></span><span class="field-arrow" style="left:143px;top:179px"></span>
  <span class="field-label" style="left:22px;top:228px">Kids</span>
  <span class="field-box" style="left:97px;top:225px"></span><span class="field-arrow" style="left:143px;top:227px"></span>
  <span class="date-box"></span>
  <svg class="calendar" viewBox="0 0 28 28" aria-hidden="true"><rect x="6" y="7" width="16" height="14" fill="#fff" stroke="#888"/><rect x="6" y="7" width="16" height="4" fill="#c0282d"/><g fill="#999"><rect x="8" y="13" width="3" height="2"/><rect x="13" y="13" width="3" height="2"/><rect x="18" y="13" width="2" height="2"/><rect x="8" y="17" width="3" height="2"/><rect x="13" y="17" width="3" height="2"/></g></svg>
  <p class="terms">By clicking this button above you’re stating that you already understand and agree to our <a href="#">Terms &amp; Conditions »</a></p>
</section>

<a class="book-btn abs" href="#">BOOK YOUR SEAT
  <svg class="book-arrow" viewBox="0 0 34 34" aria-hidden="true"><circle cx="17" cy="17" r="16" fill="#f2f2f2"/><path d="M9 14h9v-6l9 9-9 9v-6H9z" fill="#8e0a24"/></svg>
</a>

<div class="footer-rule abs"></div>
<p class="footer-info abs">© Sunvale Ride Co - Lanai Way 72-310, 11410 Oahu. Tel. ( 5550 ) 1 204 771</p>
<p class="footer-links abs"><a href="#">About Us</a> | <a href="#">FAQ</a> | <a href="#">Contact Us</a></p>

</body>
</html>
```